The Winslowe is the building name it is a luxury Coop in the city .

I manage a Coop in the City and need a business card that is simple but sharpe. I read architectural drawing, manage a full service building staff, we make repairs , we order supplies, etc . I need a card and a logo design the reflex what we do here and I am open to options . Colors blue , grey , stainlesss steel . Options thx

Industry/Entity Type

Property Management

Contact Information for Business Card

"The Winslowe " is the building name I think it should be on one side and all
Other information on the next .

Font styles to use
Serif

Requirements
Must have
• Building name "The Winslowe "
• My name Rob Tavener
• My email ROB41W8THAV@QUILLMAIL.COM
• Cell 646-318-5572
• Work 212-614-7790
• Fax 212-614-3158
Nice to have
• Maybe a drawing picture and tools something to that effect .

```html
<!DOCTYPE html>
<html lang="en">
<head>
<meta charset="utf-8">
<title>The Winslowe – Business Card</title>
<link href="https://fonts.googleapis.com/css2?family=Roboto+Slab:wght@700;800&display=swap" rel="stylesheet">
<style>
  :root {
    --stage: #000000;
    --card-top: #1f3c74;
    --card-bottom: #152a57;
    --blueprint: #2c5aa8;
    --silver-light: #f4f5f7;
    --silver-mid: #c9ccd2;
    --silver-dark: #8e939b;
    --rule: #e6e8ec;
  }
  * { margin: 0; padding: 0; box-sizing: border-box; }
  html, body {
    width: 1200px; height: 1000px; overflow: hidden;
    background: var(--stage);
  }
  .stage { position: relative; width: 1200px; height: 1000px; }

  .card {
    position: absolute; left: 285px; width: 630px; height: 361px;
    background: linear-gradient(180deg, var(--card-top) 0%, var(--card-bottom) 100%);
    overflow: hidden;
    font-family: "Roboto Slab", Georgia, serif;
  }
  .card--front { top: 129px; }
  .card--back { top: 530px; }

  .blueprint-art {
    position: absolute;
    background:
      radial-gradient(ellipse at 60% 60%, rgba(60,110,190,0.28), rgba(60,110,190,0) 70%);
    border-radius: 2px;
  }
  .card--front .blueprint-art { left: 20px; top: 8px; width: 600px; height: 353px; }
  .card--back .blueprint-art { left: 0; top: 0; width: 630px; height: 361px; opacity: 0.6; }

  .silver-text {
    background: linear-gradient(180deg, var(--silver-light) 0%, var(--silver-mid) 55%, var(--silver-dark) 100%);
    -webkit-background-clip: text; background-clip: text;
    color: transparent;
  }

  .building-name {
    position: absolute; left: 40px; top: 32px;
    font-size: 38px; font-weight: 800; letter-spacing: -0.5px; line-height: 1;
  }

  .manager-name {
    position: absolute; right: 338px; top: 686px; top: 156px;
    font-size: 34px; font-weight: 800; letter-spacing: -0.5px; line-height: 1;
    white-space: nowrap;
  }

  .divider {
    position: absolute; left: 313px; top: 70px; width: 2px; height: 245px;
    background: linear-gradient(180deg, rgba(230,232,236,0) 0%, var(--rule) 30%, var(--rule) 70%, rgba(230,232,236,0) 100%);
  }

  .contact-list {
    position: absolute; left: 335px; top: 128px; list-style: none;
  }
  .contact-item {
    display: flex; align-items: center; height: 25px;
  }
  .contact-icon { width: 16px; height: 16px; margin-right: 12px; flex: none; }
  .contact-text {
    font-size: 18px; font-weight: 700; letter-spacing: 0.3px; line-height: 1;
  }
  .contact-text--email { font-size: 14.5px; letter-spacing: 0.4px; }
</style>
</head>
<body>
<main class="stage">

  <section class="card card--front" aria-label="Business card front">
    <div class="blueprint-art" role="img" aria-label="Blue line drawing of the building's front elevation"></div>
    <h1 class="building-name silver-text">The Winslowe</h1>
  </section>

  <section class="card card--back" aria-label="Business card back">
    <div class="blueprint-art" role="img" aria-label="Faint blueprint detail of the building facade"></div>
    <h2 class="manager-name silver-text">Rob Tavener</h2>
    <div class="divider"></div>
    <ul class="contact-list">
      <li class="contact-item">
        <svg class="contact-icon" viewBox="0 0 16 16" aria-label="Cell">
          <rect x="4" y="1" width="8" height="14" rx="1.5" fill="none" stroke="#d6d8dc" stroke-width="1.5"/>
          <rect x="5.5" y="3" width="5" height="8" fill="#d6d8dc"/>
        </svg>
        <span class="contact-text silver-text">646-318-5572</span>
      </li>
      <li class="contact-item">
        <svg class="contact-icon" viewBox="0 0 16 16" aria-label="Work">
          <path d="M1 6 C1 2 15 2 15 6 L12 6.5 L11 4.5 L5 4.5 L4 6.5 Z" fill="#d6d8dc"/>
          <path d="M4 8 L12 8 L14 14 L2 14 Z" fill="none" stroke="#d6d8dc" stroke-width="1.4"/>
          <circle cx="8" cy="11" r="1.6" fill="#d6d8dc"/>
        </svg>
        <span class="contact-text silver-text">212-614-7790</span>
      </li>
      <li class="contact-item">
        <svg class="contact-icon" viewBox="0 0 16 16" aria-label="Fax">
          <rect x="4" y="1" width="8" height="5" fill="#d6d8dc"/>
          <rect x="1" y="6" width="14" height="6" rx="1" fill="#d6d8dc"/>
          <rect x="4" y="10" width="8" height="5" fill="#1b3468" stroke="#d6d8dc" stroke-width="1.2"/>
        </svg>
        <span class="contact-text silver-text">212-614-3158</span>
      </li>
      <li class="contact-item">
        <svg class="contact-icon" viewBox="0 0 16 16" aria-label="Email">
          <rect x="1" y="3" width="14" height="10" fill="#d6d8dc"/>
          <path d="M1 3 L8 9 L15 3 M1 13 L6 7.5 M15 13 L10 7.5" fill="none" stroke="#1b3468" stroke-width="1.2"/>
        </svg>
        <span class="contact-text contact-text--email silver-text">ROB41W8THAV@QUILLMAIL.COM</span>
      </li>
    </ul>
  </section>

</main>
</body>
</html>
```